Real Estate Webpage Design

We have an existing website: brindlewoodhomes.com.au
We focus customised service mainly on Property Management and second-hand property sales.
We are not entirely happy about the current design and layout can stay roughly the same as the back end coding is linked to a CRM system.
We would like to see the design are more reachable to our clients and appearing.
Please check our Website Design Draft for more details.

Industry/Entity Type

Real estate Agency

Number of Pages Required

5+ page

Font styles to use
Sans Serif

Colors

Designer to choose colors to be used in the design.

```html
<!DOCTYPE html>
<html lang="en">
<head>
<meta charset="utf-8">
<title>Brindlewood Homes – Property Management</title>
<link href="https://fonts.googleapis.com/css2?family=Poppins:ital,wght@0,400;0,500;0,600;0,700;0,800;0,900;1,400;1,900&display=swap" rel="stylesheet">
<style>
:root{
  --gold:#E9BC56;
  --gold-soft:#EDC66A;
  --navy:#1F2B3D;
  --ink:#1C1C1C;
  --muted:#6E6E6E;
  --white:#FFFFFF;
  --line:#D9D9D9;
}
*{box-sizing:border-box;margin:0;padding:0}
html,body{width:1200px;height:4409px;overflow:hidden}
body{font-family:'Poppins',sans-serif;color:var(--ink);background:var(--white);position:relative}
section,header,nav,footer{position:absolute;left:0;width:1200px}
.abs{position:absolute}

/* top bar */
.topbar{top:0;height:30px;background:var(--gold);font-size:9px;color:var(--ink)}
.topbar .item{display:flex;align-items:center;gap:7px;top:7px;white-space:nowrap}

/* nav */
.nav{top:30px;height:90px;background:var(--white)}
.brand{display:flex;align-items:center;gap:8px}
.brand-mark{width:34px;height:34px;background:var(--gold)}
.brand-name{font-weight:600;font-size:28px;color:var(--gold);line-height:1}
.brand-sub{font-size:8px;color:var(--navy);margin-top:2px}
.menu{display:flex;gap:30px;font-size:11px;top:42px;right:108px;white-space:nowrap}
.menu a{color:var(--ink);text-decoration:none;padding-bottom:7px}
.menu a.active{border-bottom:2px solid var(--gold)}

/* hero */
.hero{top:120px;height:573px;overflow:hidden}
.hero-photo{position:absolute;inset:0;background:linear-gradient(180deg,#3E6FB4 0%,#8FB1D9 45%,#C9CFD6 70%,#7A8189 100%)}
.hero-card{left:123px;top:140px;width:510px;height:274px;background:rgba(40,52,72,.85);padding:40px 50px}
.hero-card h1{font-size:72px;font-weight:900;font-style:italic;color:var(--white);line-height:.95;letter-spacing:-1px}
.hero-card h2{font-size:44px;font-weight:900;font-style:italic;color:var(--gold);line-height:1;margin-top:4px}
.hero-card p{font-size:11px;color:var(--white);line-height:21px;margin-top:18px}

/* about */
.about{top:693px;height:591px}
.about-visual{left:134px;top:107px;width:350px;height:350px;background:linear-gradient(135deg,#E9BC56 0%,#E9BC56 45%,#9DB4CC 46%,#D8DEE4 100%)}
.about-text{left:616px;top:120px;width:420px}
.about-text h2{font-size:48px;font-weight:600;color:var(--navy);line-height:1}
.about-text h3{font-size:19px;font-weight:600;color:var(--navy);margin-top:20px}
.about-text h3 mark{background:var(--gold);color:var(--navy);padding:0 3px}
.about-text p{font-size:11px;color:var(--muted);line-height:24px;margin-top:22px}

/* band */
.band{top:1284px;height:260px;background:linear-gradient(90deg,#E6BA57 0%,#E0B456 50%,#D8AE55 100%);overflow:hidden}
.band h2{left:138px;top:84px;font-size:36px;font-weight:700;color:var(--navy)}
.band p{left:138px;top:140px;font-size:11px;line-height:21px;color:var(--navy);width:400px}
.btn{background:var(--navy);color:var(--white);display:flex;align-items:center;justify-content:center;font-weight:500}
.band .btn{left:890px;top:107px;width:145px;height:48px;font-size:11px}

/* listings */
.listings{top:1544px;height:868px}
.listings .kicker{width:100%;text-align:center;top:108px;font-size:19px;font-weight:500;color:var(--navy)}
.listings h2{width:100%;text-align:center;top:130px;font-size:50px;font-weight:600;color:var(--navy)}
.listings h2 span{color:var(--gold)}
.tabs{display:flex;gap:48px;top:231px;left:390px;font-size:11px;color:var(--muted)}
.tabs .active{border-bottom:2px solid var(--gold);padding-bottom:4px;color:var(--ink)}
.card{top:300px;width:224px;height:436px;border:3px solid var(--navy);padding:10px 11px}
.card-photo{width:196px;height:216px;background:linear-gradient(160deg,#C9C6BE 0%,#8C7A68 60%,#6B4A33 100%)}
.card h3{font-size:20px;font-weight:600;color:var(--navy);margin-top:18px}
.card .addr{font-size:9.5px;color:var(--muted);margin-top:4px;line-height:17px}
.card .lbl{font-size:9.5px;font-weight:600;margin-top:6px}
.card .time{font-size:9.5px;color:var(--muted);margin-top:6px}
.stats{position:absolute;left:11px;bottom:11px;width:196px;height:42px;background:var(--navy);display:flex;align-items:center;justify-content:space-around;color:var(--white);font-size:10px}
.stats div{display:flex;align-items:center;gap:5px}
.stats .sep{width:1px;height:22px;background:var(--white)}

/* testimonials */
.testimonials{top:2412px;height:462px}
.t-panel{left:0;top:0;width:705px;height:462px;background:var(--gold)}
.t-photo{left:705px;top:0;width:495px;height:462px;background:linear-gradient(180deg,#EDEDEA 0%,#CFC6B6 55%,#8A6A4A 100%)}
.t-panel .kicker{left:123px;top:78px;font-size:20px;font-weight:500;color:var(--navy)}
.t-panel h2{left:121px;top:103px;font-size:48px;font-weight:700;color:var(--navy)}
.t-panel blockquote{left:120px;top:190px;width:480px;font-size:20px;font-style:italic;line-height:29px;color:var(--navy)}
.t-panel .who{left:122px;top:356px;font-size:19px;font-weight:600;color:var(--navy)}
.t-panel .who small{font-size:12px;font-weight:400;margin-left:12px}
.t-panel .quote{left:510px;top:326px;font-size:110px;font-weight:900;color:var(--navy);line-height:1}

/* contact */
.contact{top:2874px;height:704px}
.contact h2{width:100%;text-align:center;top:115px;font-size:50px;font-weight:700;color:var(--navy)}
.contact .lead{width:100%;text-align:center;top:198px;font-size:11px;line-height:24px;color:var(--muted)}
.field{width:376px;height:46px;border:2px solid var(--navy);font-size:14px;padding:11px 24px;color:var(--navy)}
.field.msg{width:376px;height:186px}
.contact .btn{left:413px;top:519px;width:375px;height:47px;font-size:15px}

/* map */
.map{top:3578px;height:372px;overflow:hidden}
.map-fill{position:absolute;inset:0;background:linear-gradient(135deg,#E8EDE6 0%,#DCE6D6 50%,#E9ECEF 100%)}

/* footer */
.footer{top:3950px;height:459px;background:var(--navy);color:var(--white)}
.footer .brand{left:193px;top:112px}
.footer .contact-line{display:flex;gap:10px;font-size:11px;line-height:24px;left:191px}
.footer h4{font-size:17px;font-weight:600}
.footer h4::after{content:"";display:block;width:52px;height:3px;background:var(--gold);margin-top:8px}
.links{display:grid;grid-template-columns:110px 110px;row-gap:14px;font-size:11px}
.socials{display:flex;gap:6px}
.socials span{width:25px;height:25px;border-radius:50%;background:var(--gold)}
.copy{width:100%;text-align:center;top:393px;font-size:11px}
</style>
</head>
<body>

<header class="topbar">
  <div class="abs item" style="left:126px">
    <svg width="14" height="14" viewBox="0 0 16 16"><path d="M3 1l3 3-2 2c1 2 4 5 6 6l2-2 3 3-2 2C7 15 1 9 1 3z" fill="none" stroke="#1F2B3D" stroke-width="1.3"/></svg>
    <span>P: 02 5550 1234</span>
  </div>
  <div class="abs item" style="left:258px">
    <svg width="13" height="15" viewBox="0 0 14 16"><path d="M7 15s5-5 5-9A5 5 0 0 0 2 6c0 4 5 9 5 9z" fill="none" stroke="#1F2B3D" stroke-width="1.3"/><circle cx="7" cy="6" r="2" fill="none" stroke="#1F2B3D" stroke-width="1.3"/></svg>
    <span>18/4 Wattlebird Lane, Harrowfield, ACT, 2990</span>
  </div>
  <div class="abs item" style="left:940px;top:6px">
    <svg width="18" height="18" viewBox="0 0 18 18"><circle cx="7.5" cy="7.5" r="5.5" fill="none" stroke="#1F2B3D" stroke-width="2.2"/><path d="M12 12l5 5" stroke="#1F2B3D" stroke-width="2.5"/></svg>
  </div>
  <div class="abs item" style="left:982px">
    <svg width="22" height="16" viewBox="0 0 22 16"><rect x="1" y="1" width="20" height="14" fill="none" stroke="#1F2B3D" stroke-width="1.3"/><circle cx="7" cy="7" r="2.3" fill="none" stroke="#1F2B3D" stroke-width="1.2"/><path d="M12 6h6M12 9h6M4 12h7" stroke="#1F2B3D" stroke-width="1.2"/></svg>
    <span>Login / Signup</span>
  </div>
</header>

<nav class="nav">
  <div class="abs brand" style="left:125px;top:28px">
    <div class="brand-mark"></div>
    <div>
      <div class="brand-name">Brindlewood</div>
      <div class="brand-sub">Property Group</div>
    </div>
  </div>
  <div class="abs menu">
    <a class="active">Home</a><a>About Us</a><a>Leasing</a><a>Buy</a><a>Sell</a><a>Our Team</a><a>Blog</a><a>Contact Us</a>
  </div>
</nav>

<section class="hero">
  <div class="hero-photo" role="img" aria-label="Photo of a modern white multi-storey house under a blue sky"></div>
  <div class="abs hero-card">
    <h1>PROPERTY</h1>
    <h2>MANAGEMENT</h2>
    <p>Brindlewood is named for “the home, the house”, buying a property is<br>one of the most expensive expenses and important assets.</p>
  </div>
  <svg class="abs" style="left:0;top:500px" width="1200" height="73" viewBox="0 0 1200 73">
    <path d="M0 73V20L600 60 1200 15V73z" fill="#FFFFFF"/>
    <path d="M0 18L600 58 1200 13V22L600 70 0 30z" fill="#E9BC56"/>
  </svg>
</section>

<section class="about">
  <div class="abs about-visual" role="img" aria-label="Photo of a modern home entrance framed in gold and navy blocks"></div>
  <div class="abs about-text">
    <h2>Brindlewood</h2>
    <h3>A name for <mark>“the home”</mark></h3>
    <p>Brindlewood is named for “the home, the house”, buying a property is one of the most expensive expenses and important assets for people. Brindlewood is a real estate company located in Harrowfield, Canberra.</p>
    <p style="margin-top:16px">Being a portfolio sales agent and property manager, coupled with our high–profile international real estate experience, Brindlewood is considered a market leader on the cutting edge with deep industry knowledge, ranging from landlord–tenant relationships, residential purchases.</p>
  </div>
</section>

<section class="band" role="img" aria-label="Gold-tinted photo of apartment building facades">
  <h2 class="abs">Second-hand property sales</h2>
  <p class="abs">Brindlewood is named for “the home, the house”, buying a property is one of the most expensive expenses and important assets.</p>
  <div class="abs btn">Contact Us</div>
</section>

<section class="listings">
  <div class="abs kicker">This Month At</div>
  <h2 class="abs">Brindlewood <span>Homes</span></h2>
  <div class="abs tabs"><span>For Sale</span><span class="active">For Lease</span><span>Open Times</span><span>Sold</span><span>Leased</span></div>

  <div class="abs card" style="left:120px">
    <div class="card-photo" role="img" aria-label="Photo of a living room with timber floor"></div>
    <h3>Lawson</h3>
    <div class="addr">12/40 Ridgeview Terrace Lawson<br>$640 - $660 pw</div>
    <div class="lbl">Next Inspection:</div>
    <div class="time">Sat 21st May 02:30 PM - 02:45 PM</div>
    <div class="stats"><div>3 <svg width="16" height="10"><path d="M1 9V1M1 6h14v3M4 6V3h5v3" stroke="#fff" fill="none"/></svg></div><span class="sep"></span><div>2 <svg width="16" height="10"><path d="M1 5h14v2a3 3 0 0 1-3 3H4a3 3 0 0 1-3-3zM3 5V1h2" stroke="#fff" fill="none"/></svg></div><span class="sep"></span><div>2 <svg width="16" height="12"><path d="M2 10V6l2-4h8l2 4v4zM2 6h12" stroke="#fff" fill="none"/></svg></div></div>
  </div>
  <div class="abs card" style="left:366px">
    <div class="card-photo" role="img" aria-label="Photo of a bright lounge with sofas" style="background:linear-gradient(160deg,#E9E6DE 0%,#B9A68C 60%,#7E6A52 100%)"></div>
    <h3>Red Hill</h3>
    <div class="addr">12/40 Ridgeview Terrace Lawson<br>$640 - $660 pw</div>
    <div class="lbl">Next Inspection:</div>
    <div class="time">Sat 21st May 02:30 PM - 02:45 PM</div>
    <div class="stats"><div>3 <svg width="16" height="10"><path d="M1 9V1M1 6h14v3M4 6V3h5v3" stroke="#fff" fill="none"/></svg></div><span class="sep"></span><div>2 <svg width="16" height="10"><path d="M1 5h14v2a3 3 0 0 1-3 3H4a3 3 0 0 1-3-3zM3 5V1h2" stroke="#fff" fill="none"/></svg></div><span class="sep"></span><div>2 <svg width="16" height="12"><path d="M2 10V6l2-4h8l2 4v4zM2 6h12" stroke="#fff" fill="none"/></svg></div></div>
  </div>
  <div class="abs card" style="left:611px">
    <div class="card-photo" role="img" aria-label="Photo of a dining room with white chairs" style="background:linear-gradient(160deg,#D8D2C6 0%,#A89680 60%,#6E5640 100%)"></div>
    <h3>Braddon</h3>
    <div class="addr">12/40 Ridgeview Terrace Lawson<br>$640 - $660 pw</div>
    <div class="lbl">Next Inspection:</div>
    <div class="time">Sat 21st May 02:30 PM - 02:45 PM</div>
    <div class="stats"><div>3 <svg width="16" height="10"><path d="M1 9V1M1 6h14v3M4 6V3h5v3" stroke="#fff" fill="none"/></svg></div><span class="sep"></span><div>2 <svg width="16" height="10"><path d="M1 5h14v2a3 3 0 0 1-3 3H4a3 3 0 0 1-3-3zM3 5V1h2" stroke="#fff" fill="none"/></svg></div><span class="sep"></span><div>2 <svg width="16" height="12"><path d="M2 10V6l2-4h8l2 4v4zM2 6h12" stroke="#fff" fill="none"/></svg></div></div>
  </div>
  <div class="abs card" style="left:856px">
    <div class="card-photo" role="img" aria-label="Photo of a living room with timber floor"></div>
    <h3>Griffith</h3>
    <div class="addr">12/40 Ridgeview Terrace Lawson<br>$640 - $660 pw</div>
    <div class="lbl">Next Inspection:</div>
    <div class="time">Sat 21st May 02:30 PM - 02:45 PM</div>
    <div class="stats"><div>3 <svg width="16" height="10"><path d="M1 9V1M1 6h14v3M4 6V3h5v3" stroke="#fff" fill="none"/></svg></div><span class="sep"></span><div>2 <svg width="16" height="10"><path d="M1 5h14v2a3 3 0 0 1-3 3H4a3 3 0 0 1-3-3zM3 5V1h2" stroke="#fff" fill="none"/></svg></div><span class="sep"></span><div>2 <svg width="16" height="12"><path d="M2 10V6l2-4h8l2 4v4zM2 6h12" stroke="#fff" fill="none"/></svg></div></div>
  </div>
</section>

<section class="testimonials">
  <div class="abs t-panel">
    <div class="abs kicker">What others Say</div>
    <h2 class="abs">Testimonials</h2>
    <blockquote class="abs">Jenna is my best property manager! Always happy to response my queries and keep us well informed at all stage.&nbsp; I will definitely recommend her to my friends.</blockquote>
    <div class="abs who">Marcus Hale <small>- Client</small></div>
    <div class="abs quote">”</div>
  </div>
  <div class="abs t-photo" role="img" aria-label="Photo of a sunlit lounge with brown sofas and teal cushions"></div>
</section>

<section class="contact">
  <h2 class="abs">Contact Form</h2>
  <p class="abs lead">Brindlewood is named for “the home, the house”, buying a property is one of the most expensive expenses<br>and important assets for people. Brindlewood is a real estate company located.</p>
  <div class="abs field" style="left:214px;top:288px">Name</div>
  <div class="abs field" style="left:214px;top:358px">Email</div>
  <div class="abs field" style="left:214px;top:428px">Subject</div>
  <div class="abs field msg" style="left:618px;top:288px">Message</div>
  <div class="abs btn">Contact Us</div>
</section>

<section class="map">
  <div class="map-fill" role="img" aria-label="Street map showing the office location"></div>
  <svg class="abs" style="left:0;top:0" width="1200" height="60" viewBox="0 0 1200 60">
    <path d="M0 0H1200V22L600 2 0 42z" fill="#FFFFFF"/>
    <path d="M0 40L600 0 1200 20V30L600 12 0 50z" fill="#E9BC56"/>
  </svg>
</section>

<footer class="footer">
  <div class="abs brand">
    <div class="brand-mark" style="width:40px;height:40px"></div>
    <div>
      <div class="brand-name" style="font-size:34px">Brindlewood</div>
      <div class="brand-sub" style="color:#fff">Property Group</div>
    </div>
  </div>
  <div class="abs contact-line" style="top:206px">
    <svg width="14" height="16" viewBox="0 0 14 16" style="margin-top:4px"><path d="M7 15s5-5 5-9A5 5 0 0 0 2 6c0 4 5 9 5 9z" fill="none" stroke="#E9BC56" stroke-width="1.3"/><circle cx="7" cy="6" r="2" fill="none" stroke="#E9BC56" stroke-width="1.3"/></svg>
    <span>18/4 Wattlebird Lane,<br>Harrowfield, ACT, 2990</span>
  </div>
  <div class="abs contact-line" style="top:278px">
    <svg width="16" height="16" viewBox="0 0 16 16" style="margin-top:4px"><path d="M3 1l3 3-2 2c1 2 4 5 6 6l2-2 3 3-2 2C7 15 1 9 1 3z" fill="none" stroke="#E9BC56" stroke-width="1.3"/></svg>
    <span>P: 02 5550 1234</span>
  </div>
  <div class="abs contact-line" style="top:302px">
    <svg width="16" height="16" viewBox="0 0 16 16" style="margin-top:4px"><rect x="1" y="5" width="14" height="9" fill="none" stroke="#E9BC56" stroke-width="1.3"/><rect x="4" y="1" width="8" height="4" fill="none" stroke="#E9BC56" stroke-width="1.3"/></svg>
    <span>F: 02 5550 1298</span>
  </div>

  <div class="abs" style="left:554px;top:114px">
    <h4>Pages</h4>
    <div class="links" style="margin-top:28px">
      <span>Home</span><span>Our Team</span>
      <span>About Us</span><span>Blog</span>
      <span>Leasing</span><span>Contact Us</span>
      <span>Buy</span><span></span>
      <span>Sell</span><span></span>
    </div>
  </div>

  <div class="abs" style="left:885px;top:114px">
    <h4>Social Media</h4>
    <div class="socials" style="margin-top:24px"><span></span><span></span><span></span><span></span><span></span></div>
  </div>

  <div class="abs copy">Copyright © 2022 All rights reserved &nbsp;|&nbsp; Privacy Policy</div>
</footer>

</body>
</html>
```